VORKEL COMPOSITES INC website in USA

VORKEL COMPOSITES INC incorporated and operated in USA needs a completely new design of website. This Wyoming based company is a importer and distributor of composites material to supply mainly to American and Canadian/Mexican customers. Our main products includes Carbon Fiber, Aramid Fiber, Glass Fiber, Basalt Fiber, High Silica Glass, Quartz Fiber, S-Glass, Alumina Fiber, Vacuum Auxiliary.

We are one stop composites solution provider for Automotive, Aerospace, Construction, Electrical and Machinery industries.

We are exclusive sales company in North America for DORAQ composites produced from China and their other Asia facilities.

Target Market(s)

USA and Canada

Industry/Entity Type

Composites materials

Coding

Coded - Design and coding required

Number of Pages Required

5+ page

Requirements
Nice to have
• Color theme to match our corporate logo VORKEL. VORKEL stands for Vantor Omniline Reliant Kinetic Export Lodge

```html
<!DOCTYPE html>
<html lang="en">
<head>
<meta charset="utf-8">
<title>VORKEL COMPOSITES INC</title>
<link rel="stylesheet" href="https://fonts.googleapis.com/css2?family=Barlow+Condensed:ital,wght@0,600;0,700;1,700;1,800&family=Inter:wght@400;500;600;700&display=swap">
<style>
:root{
  --stage:#d3d3d3;
  --ink:#2b2b2c;
  --ink-2:#252526;
  --ink-3:#303031;
  --orange:#f39a2a;
  --white:#ffffff;
  --dark-text:#1e1e1e;
}
*{box-sizing:border-box;margin:0;padding:0}
html,body{width:1200px;height:2788px;overflow:hidden;background:var(--stage)}
body{font-family:"Inter",Arial,sans-serif;color:var(--white);position:relative}
.page{position:absolute;left:81px;top:81px;width:1038px;height:2624px;background:var(--ink);overflow:hidden;box-shadow:0 6px 24px rgba(0,0,0,.25)}
.abs{position:absolute}

/* header */
.brand{left:34px;top:22px;display:flex;align-items:center;gap:14px}
.brand-name{font-family:"Barlow Condensed",Arial Narrow,sans-serif;font-weight:700;font-size:42px;color:var(--white);letter-spacing:1px;line-height:1}
.brand-sep{width:1px;height:56px;background:var(--white)}
.brand-tag{font-size:9px;font-style:italic;line-height:1.25;width:110px}
.nav{right:140px;top:24px;display:flex;gap:28px;font-family:"Barlow Condensed",sans-serif;font-weight:700;font-size:12px}
.nav-cta{left:923px;top:16px;width:96px;height:27px;background:var(--orange);color:var(--dark-text);font-family:"Barlow Condensed",sans-serif;font-weight:700;font-size:11.5px;display:flex;align-items:center;justify-content:center}

/* hero */
.hero-backdrop{left:0;top:330px;width:700px;height:200px;background:linear-gradient(180deg,rgba(43,43,44,1) 0%,rgba(70,72,78,.7) 55%,rgba(43,43,44,1) 100%)}
.hero-rule{left:36px;top:145px;width:2px;height:183px;background:var(--white);transform:skewX(-6deg)}
.hero-title{left:62px;top:152px;font-family:"Barlow Condensed",sans-serif;font-style:italic;font-weight:800;font-size:40px;line-height:40px;text-transform:uppercase}
.hero-title span{display:block}
.hero-title .l1{color:var(--white)}
.hero-title .l2{color:var(--orange);margin-left:-6px}
.hero-title .l3{color:var(--orange);margin-left:-12px}
.hero-lede{left:55px;top:282px;width:420px;font-size:11px;font-style:italic;line-height:21px}
.btn{height:38px;border-radius:19px;display:flex;align-items:center;justify-content:center;font-size:12px;font-weight:600}
.btn-primary{left:34px;top:346px;width:154px;background:var(--orange);color:var(--dark-text)}
.btn-ghost{left:197px;top:346px;width:154px;border:1.5px solid var(--orange);color:var(--white)}
.hero-photo{left:581px;top:92px;width:463px;height:427px;border-radius:50%;background:radial-gradient(ellipse at 55% 30%,#c9d3dc 0%,#a5b1bc 40%,#6f7780 75%,#555a60 100%);border:6px solid var(--orange)}

/* sections */
.section-title{left:0;width:1038px;text-align:center;font-family:"Barlow Condensed",sans-serif;font-weight:700;font-size:32px;text-transform:uppercase}
.section-title .accent{color:var(--orange)}
.grid{left:87px;width:864px;display:grid;grid-template-columns:repeat(3,288px)}
.card{height:174px;display:flex;flex-direction:column;align-items:center;text-align:center;padding:22px 18px 0}
.card.dark{background:var(--ink-3)}
.card.deep{background:var(--ink-2)}
.card.orange{background:var(--orange)}
.card svg{width:48px;height:48px;fill:none;stroke:var(--orange);stroke-width:1.6;stroke-linecap:round;stroke-linejoin:round}
.card.orange svg{stroke:var(--white)}
.card h3{font-family:"Barlow Condensed",sans-serif;font-weight:700;font-size:19px;color:var(--orange);margin-top:14px;line-height:1}
.card.orange h3{color:var(--white)}
.card p{font-size:10.5px;line-height:18px;margin-top:8px;color:var(--white)}
.card.orange p{color:#fff6e6}
.why .card{height:192px;padding:22px 16px 0}

.products-bg{left:0;top:957px;width:1038px;height:637px;background:linear-gradient(180deg,#2a2a2b 0%,#2a2a2b 70%,#3a3d42 100%)}
.products-photo{left:0;top:1450px;width:1038px;height:144px;background:linear-gradient(180deg,rgba(42,42,43,.2),#4a4f56 60%,#3b3e43)}

.cta-band{left:0;top:1594px;width:1038px;height:195px;background:linear-gradient(100deg,#f4a23a 0%,#f5ad52 45%,#f39a2a 100%)}
.cta-text{left:0;top:1630px;width:1038px;text-align:center;font-family:"Barlow Condensed",sans-serif;font-weight:700;font-size:30px;line-height:34px;color:var(--white)}
.cta-btn{left:438px;top:1713px;width:160px;height:39px;background:var(--dark-text);color:var(--orange);font-family:"Barlow Condensed",sans-serif;font-weight:700;font-size:15px;display:flex;align-items:center;justify-content:center}

.industries-bg{left:0;top:1789px;width:1038px;height:155px;background:linear-gradient(180deg,#3d4045 0%,#34373b 60%,#2b2b2c 100%)}

/* footer */
.footer{left:0;top:2373px;width:1038px;height:251px;background:linear-gradient(180deg,#2d2e30,#323337)}
.foot-brand{left:87px;top:2440px;display:flex;align-items:center;gap:10px}
.foot-brand .brand-name{font-size:34px}
.foot-brand .brand-sep{height:44px}
.foot-brand .brand-tag{font-size:7.5px;width:80px}
.foot-about{left:87px;top:2500px;width:220px;font-size:9.5px;line-height:16px}
.foot-head{font-family:"Barlow Condensed",sans-serif;font-weight:700;font-size:17px;text-transform:uppercase}
.foot-head .accent{color:var(--orange)}
.foot-list{list-style:none;font-size:9.5px;line-height:16.5px;margin-top:14px}
.foot-list li::before{content:"\2605";color:var(--orange);margin-right:6px;font-size:8px}
.contact-line{display:flex;align-items:center;gap:6px}
.contact-line svg{width:10px;height:10px;fill:none;stroke:var(--orange);stroke-width:1.4}
.foot-copy{left:797px;top:2502px;font-size:9.5px;line-height:16.5px}
</style>
</head>
<body>
<div class="page">

  <div class="abs brand">
    <span class="brand-name">VORKEL</span>
    <span class="brand-sep"></span>
    <span class="brand-tag">Vantor Omniline Reliant Kinetic Export Lodge</span>
  </div>
  <nav class="abs nav"><span>Home</span><span>Products</span><span>Industries</span><span>About</span><span>Contact</span></nav>
  <div class="abs nav-cta">REQUEST A QUOTE</div>

  <div class="abs hero-backdrop" role="img" aria-label="Faded photo of a container port with cargo ships and stacked containers"></div>
  <div class="abs hero-rule"></div>
  <h1 class="abs hero-title"><span class="l1">One-stop composites supply</span><span class="l2">for aerospace, automotive,</span><span class="l3">construction &amp; energy</span></h1>
  <p class="abs hero-lede">Stock + custom weaves, unidirectional, multiaxials, and high-temp fibers with technical documentation, QA traceability, and North American logistics.</p>
  <div class="abs btn btn-primary">BROWSE PRODUCTS</div>
  <div class="abs btn btn-ghost">REQUEST A QUOTE</div>
  <div class="abs hero-photo" role="img" aria-label="Photo of a passenger jet on the apron with a ground worker in a safety vest"></div>

  <h2 class="abs section-title" style="top:612px">Why <span class="accent">Vorkel</span></h2>
  <div class="abs grid why" style="top:682px">
    <div class="card dark">
      <svg viewBox="0 0 48 48" role="img" aria-label="Access icon"><circle cx="24" cy="16" r="8"/><path d="M24 24v14M18 32h12M10 10h6M32 10h6M10 22h5M33 22h5"/></svg>
      <h3>Exclusive DORAQ Access</h3>
      <p>Priority access to DORAQ composite lines manufactured in Asia with QA traceability and export documentation tuned for North America.</p>
    </div>
    <div class="card orange">
      <svg viewBox="0 0 48 48" role="img" aria-label="Catalog icon"><rect x="10" y="8" width="28" height="32" rx="2"/><path d="M16 16h16M16 23h16M16 30h10"/></svg>
      <h3>Engineering-grade Catalog</h3>
      <p>From PAN-based carbon to high-temperature silica and alumina fibers, our breadth covers performance, process, and budget envelopes.</p>
    </div>
    <div class="card dark">
      <svg viewBox="0 0 48 48" role="img" aria-label="Processing icon"><rect x="8" y="8" width="13" height="20"/><rect x="27" y="8" width="13" height="20"/><path d="M14 28v8h20v-8M10 40h28"/></svg>
      <h3>Vacuum &amp; Processing</h3>
      <p>Vacuum bagging films, peel plies, release media, and ancillary supplies for prepreg, infusion, and OOA processes—bundled to your BOM.</p>
    </div>
  </div>

  <div class="abs products-bg"></div>
  <div class="abs products-photo" role="img" aria-label="Faded photo of an aircraft on the apron with a ground worker"></div>
  <h2 class="abs section-title" style="top:1031px">Core <span class="accent">Product Families</span></h2>
  <div class="abs grid" style="top:1103px">
    <div class="card orange">
      <svg viewBox="0 0 48 48" role="img" aria-label="Carbon fiber icon"><path d="M14 28a8 8 0 1 1 4-15 9 9 0 0 1 16 3 6 6 0 0 1 0 12z"/><path d="M18 30v10M24 30v10M30 30v10"/></svg>
      <h3>Carbon Fiber</h3>
      <p>Woven, UD, multiaxial, and prepreg-ready reinforcements for structural applications.</p>
    </div>
    <div class="card deep">
      <svg viewBox="0 0 48 48" role="img" aria-label="Aramid weave icon"><path d="M8 14h32M8 24h32M8 34h32M14 8v32M24 8v32M34 8v32"/></svg>
      <h3>Aramid Fiber</h3>
      <p>Impact-resistant fabrics for ballistic and abrasion environments.</p>
    </div>
    <div class="card orange">
      <svg viewBox="0 0 48 48" role="img" aria-label="Glass panel icon"><rect x="10" y="8" width="28" height="32"/><path d="M18 30l12-12M22 36l10-10"/></svg>
      <h3>Glass &amp; S-Glass</h3>
      <p>E-glass and S-glass options balancing cost and performance.</p>
    </div>
    <div class="card deep">
      <svg viewBox="0 0 48 48" role="img" aria-label="Fabric roll icon"><rect x="12" y="8" width="10" height="32" rx="5"/><path d="M22 20h16v20H17M28 26v10M33 26v10M24 31h14"/></svg>
      <h3>Carbon Fiber</h3>
      <p>Woven, UD, multiaxial, and prepreg-ready reinforcements for structural applications.</p>
    </div>
    <div class="card orange">
      <svg viewBox="0 0 48 48" role="img" aria-label="Crystal fiber icon"><path d="M16 14l8-6 8 6v18l-8 8-8-8z"/><path d="M24 8v32M16 14l16 18M32 14L16 32"/></svg>
      <h3>Aramid Fiber</h3>
      <p>Impact-resistant fabrics for ballistic and abrasion environments.</p>
    </div>
    <div class="card deep">
      <svg viewBox="0 0 48 48" role="img" aria-label="Fiber bundle icon"><path d="M10 34l24-24M14 38l24-24M8 28l20-20"/><circle cx="36" cy="12" r="4"/></svg>
      <h3>Glass &amp; S-Glass</h3>
      <p>E-glass and S-glass options balancing cost and performance.</p>
    </div>
  </div>

  <div class="abs cta-band"></div>
  <p class="abs cta-text">Need specification support? Our team can map your mechanical<br>targets to the right fiber/weave and process route.</p>
  <div class="abs cta-btn">TALK TO ENGINEERING</div>

  <div class="abs industries-bg" role="img" aria-label="Faded photo of aircraft fuselages in a hangar"></div>
  <h2 class="abs section-title" style="top:1873px">Industries <span class="accent">Served</span></h2>
  <div class="abs grid" style="top:1944px">
    <div class="card orange">
      <svg viewBox="0 0 48 48" role="img" aria-label="Aerospace icon"><circle cx="24" cy="24" r="15"/><path d="M24 12l5 14h-10zM20 30l-3 6M28 30l3 6"/></svg>
      <h3>Aerospace</h3>
      <p>Woven, UD, multiaxial, and prepreg-ready reinforcements for structural applications.</p>
    </div>
    <div class="card deep">
      <svg viewBox="0 0 48 48" role="img" aria-label="Automotive icon"><path d="M8 30l4-9h24l4 9v6H8z"/><circle cx="16" cy="36" r="3"/><circle cx="32" cy="36" r="3"/></svg>
      <h3>Automotive</h3>
      <p>Body panels, monocoques, interior<br>trims, and tooling.</p>
    </div>
    <div class="card orange">
      <svg viewBox="0 0 48 48" role="img" aria-label="Construction icon"><path d="M12 40V10M12 10l8 6M24 40a10 10 0 0 1 20 0z"/><circle cx="36" cy="14" r="5"/></svg>
      <h3>Construction</h3>
      <p>Rebar wraps, FRP plates,<br>strengthening systems.</p>
    </div>
    <div class="card deep">
      <svg viewBox="0 0 48 48" role="img" aria-label="Electrical icon"><path d="M30 40l4-30 4 30M31 24h6M8 40V26l8-6v6l8-6v20z"/></svg>
      <h3>Electrical</h3>
      <p>Dielectric laminates and thermal<br>insulation stacks.</p>
    </div>
    <div class="card orange">
      <svg viewBox="0 0 48 48" role="img" aria-label="Machinery icon"><circle cx="18" cy="18" r="7"/><circle cx="32" cy="32" r="7"/><path d="M18 8v3M18 25v3M8 18h3M25 18h3M32 22v3M32 39v3M22 32h3M39 32h3"/></svg>
      <h3>Machinery</h3>
      <p>Lightweight arms, guards, and<br>high-temp housings.</p>
    </div>
    <div class="card deep">
      <svg viewBox="0 0 48 48" role="img" aria-label="Energy icon"><path d="M14 40V18M14 18l-6-6M14 18l7-4M14 18v-8"/><rect x="22" y="28" width="18" height="12"/><circle cx="36" cy="12" r="4"/></svg>
      <h3>Energy</h3>
      <p>Wind blades, tanks, and<br>insulation jackets.</p>
    </div>
  </div>

  <div class="abs footer" role="img" aria-label="Faded photo of a hangar interior"></div>
  <div class="abs foot-brand">
    <span class="brand-name">VORKEL</span>
    <span class="brand-sep"></span>
    <span class="brand-tag">Vantor Omniline Reliant Kinetic Export Lodge</span>
  </div>
  <p class="abs foot-about">VORKEL COMPOSITES INC is incorporated in Wyoming, USA and serves customers across the United States, Canada, and Mexico.</p>

  <div class="abs" style="left:397px;top:2460px">
    <div class="foot-head">Explore</div>
    <ul class="foot-list"><li>Product Catalog</li><li>Industries</li><li>About</li><li>Contact</li></ul>
  </div>

  <div class="abs" style="left:576px;top:2460px">
    <div class="foot-head">Head<span class="accent">office</span></div>
    <div class="foot-list">
      <div class="contact-line"><svg viewBox="0 0 10 10"><circle cx="5" cy="3" r="2"/><path d="M1 9c0-3 8-3 8 0"/></svg>Redfield, USA</div>
      <div class="contact-line"><svg viewBox="0 0 10 10"><rect x="1" y="2" width="8" height="6"/><path d="M1 2l4 3 4-3"/></svg>sales@vorkelcomposites.com</div>
      <div class="contact-line"><svg viewBox="0 0 10 10"><path d="M2 1l2 2-1 1.5a5 5 0 0 0 2.5 2.5L7 6l2 2-1 1.5C4 9 1 6 .5 2z"/></svg>+1 (307) 555-0148</div>
    </div>
  </div>

  <p class="abs foot-copy">© 2025<br>VORKEL COMPOSITES INC.<br>All rights reserved.</p>
</div>
</body>
</html>
```